New Business Cards / Logo update

Logo:
can be updated but wanted pricing

New Business Cards:
take our existing business cards and upgrade them from a design perspective. We have two versions
Inside sales team does not have a cell phone and they use an appointment back slot.
Outside project managers and leadership uses a slogan backing and will have cell phones.

```html
<!DOCTYPE html>
<html lang="en">
<head>
<meta charset="utf-8">
<title>Harbor Carpet + Flooring – Business Cards</title>
<link href="https://fonts.googleapis.com/css2?family=Libre+Baskerville:wght@400;700&family=Open+Sans:wght@400;600&display=swap" rel="stylesheet">
<style>
  :root {
    --page-bg: #d9d9d9;
    --card-bg: #f7f7f6;
    --brand-orange: #d9861a;
    --ink-dark: #3a3a3a;
    --ink-grey: #8c8784;
    --rule: #9a948f;
  }
  * { box-sizing: border-box; margin: 0; padding: 0; }
  html, body { width: 1200px; height: 900px; overflow: hidden; }
  body {
    background: var(--page-bg);
    position: relative;
    font-family: "Open Sans", Arial, sans-serif;
  }
  .card {
    position: absolute;
    left: 285px;
    width: 630px;
    height: 360px;
    background: var(--card-bg);
    box-shadow: 0 6px 18px rgba(0,0,0,.18);
  }
  .card--appointment { top: 60px; }
  .card--contact { top: 480px; }

  .brand {
    position: absolute;
    top: 34px;
    right: 40px;
    display: flex;
    align-items: center;
    gap: 10px;
    font-family: "Libre Baskerville", Georgia, serif;
    font-weight: 400;
    font-size: 22px;
    color: var(--brand-orange);
  }
  .brand__dot {
    width: 12px; height: 12px;
    border-radius: 50%;
    background: var(--brand-orange);
  }

  /* appointment side */
  .slogan {
    position: absolute;
    left: 40px; top: 130px;
    font-family: "Libre Baskerville", Georgia, serif;
    font-weight: 700;
    font-size: 22px;
    color: var(--brand-orange);
  }
  .slogan-rule {
    position: absolute;
    left: 560px; right: 40px; top: 148px;
    border-top: 1px solid var(--rule);
  }
  .field {
    position: absolute;
    display: flex;
    align-items: baseline;
    gap: 8px;
  }
  .field__line { flex: 1; border-bottom: 1px solid var(--rule); transform: translateY(-4px); }
  .field--appointment {
    left: 40px; right: 40px; top: 180px;
    font-family: "Libre Baskerville", Georgia, serif;
    font-size: 17px; color: var(--ink-dark);
  }
  .field--date { left: 40px; width: 330px; top: 228px; }
  .field--time { left: 390px; right: 40px; top: 228px; }
  .field--date, .field--time { font-size: 15px; color: var(--ink-grey); }
  .website {
    position: absolute;
    left: 40px; bottom: 40px;
    font-size: 15px;
    font-weight: 600;
    letter-spacing: 0.32em;
    color: var(--ink-dark);
  }
  .website__domain { color: var(--brand-orange); }

  /* contact side */
  .person {
    position: absolute;
    left: 40px; right: 40px; top: 150px;
    display: flex; align-items: flex-end; gap: 12px;
  }
  .person__name {
    font-family: "Libre Baskerville", Georgia, serif;
    font-weight: 700;
    font-size: 24px;
    color: var(--brand-orange);
  }
  .person__title { font-size: 14px; color: var(--ink-grey); margin-top: 2px; }
  .person__rule { flex: 1; border-bottom: 1px solid var(--rule); margin-bottom: 10px; }
  .contact-list {
    position: absolute;
    left: 40px; top: 240px;
    list-style: none;
    font-size: 15px;
    color: var(--ink-dark);
  }
  .contact-list li { display: flex; align-items: center; gap: 10px; margin-bottom: 8px; }
  .contact-list svg { width: 16px; height: 16px; fill: var(--brand-orange); flex: none; }
</style>
</head>
<body>

<section class="card card--appointment">
  <div class="brand"><span class="brand__dot"></span>Harbor Carpet + Flooring</div>
  <p class="slogan">Quality flooring at an affordable price.</p>
  <div class="slogan-rule"></div>
  <div class="field field--appointment">Appointment<span class="field__line"></span></div>
  <div class="field field--date">Date:<span class="field__line"></span></div>
  <div class="field field--time">Time:<span class="field__line"></span></div>
  <p class="website">www.<span class="website__domain">harborfloorco</span>.com</p>
</section>

<section class="card card--contact">
  <div class="brand"><span class="brand__dot"></span>Harbor Carpet + Flooring</div>
  <div class="person">
    <div>
      <h1 class="person__name">Dana Whitfield</h1>
      <p class="person__title">Sales + Design Manager</p>
    </div>
    <span class="person__rule"></span>
  </div>
  <ul class="contact-list">
    <li>
      <svg viewBox="0 0 24 24" aria-hidden="true"><path d="M6.6 10.8a15.1 15.1 0 0 0 6.6 6.6l2.2-2.2a1 1 0 0 1 1-.25 11.4 11.4 0 0 0 3.6.57 1 1 0 0 1 1 1V20a1 1 0 0 1-1 1A17 17 0 0 1 3 4a1 1 0 0 1 1-1h3.5a1 1 0 0 1 1 1c0 1.25.2 2.45.57 3.6a1 1 0 0 1-.25 1z"/></svg>
      555·210·3344
    </li>
    <li>
      <svg viewBox="0 0 24 24" aria-hidden="true"><path d="M2 5h20v14H2z M2 5l10 8 10-8" /></svg>
      dana@harborfloorco.com
    </li>
    <li>
      <svg viewBox="0 0 24 24" aria-hidden="true"><path d="M12 2a7 7 0 0 0-7 7c0 5.2 7 13 7 13s7-7.8 7-13a7 7 0 0 0-7-7zm0 9.5A2.5 2.5 0 1 1 12 6.5a2.5 2.5 0 0 1 0 5z"/></svg>
      1420 Bayview Ln · Port Alder, FL 33900
    </li>
  </ul>
</section>

</body>
</html>
```